Kampagne Stuzzichini
Zielgruppe
Wir Haben ein Restaurant unsere Spezialität ist vorwiegend Italienischer Küche.
Für diese Kampagne wohlen wir hauptsächlich Firmenkunden und Leute duzu bewegen das Sie nach der arbeit, zu uns kommen um einen Apero Zu nehmen ansprechen.
Text:
STUZZICHINI (Überschrift)
Den typischen Apéro aus Italien gibt's Dienstags - Donnerstag ab 17.30 bis 19.00 Uhr zu jedem Getränk Gratis Dazu.
Von Foccacia über Oliven bis zu Lachsbrötchen- lassen Sie sich jede Woche von neuen Leckerbissen aus der Küche der Restaurant Tovelo überraschen!
Formate:
Postkarte A6
Volage ist vorhanden
Vorlage mit Verschnitt ist vorhanden.
-Booksmarke 75x210
Vorlage mit verschnitt ist vorhanden.
Ich lade verschiedenen Flyer hoch zur Orientation von style

```html
<!DOCTYPE html>
<html lang="de">
<head>
<meta charset="utf-8">
<title>Stuzzichini – Restaurant Tovelo</title>
<link rel="stylesheet" href="https://fonts.googleapis.com/css2?family=Advent+Pro:wght@300;400&family=Dosis:wght@700;800&family=Yanone+Kaffeesatz:wght@300;400;700&display=swap">
<style>
  :root {
    --wood-light: #eadcc6;
    --wood-mid: #dccbb0;
    --wood-dark: #c9b494;
    --ink: #3b312a;
    --accent: #e5552f;
  }
  * { margin: 0; padding: 0; box-sizing: border-box; }
  html, body { width: 1200px; height: 3199px; overflow: hidden; }
  body { position: relative; background: var(--wood-mid); color: var(--ink); }
  .wood-surface {
    position: absolute; inset: 0;
    background:
      radial-gradient(ellipse at 50% 55%, rgba(255,250,240,0.45) 0%, rgba(255,250,240,0) 60%),
      linear-gradient(180deg, var(--wood-mid) 0%, var(--wood-light) 45%, var(--wood-light) 70%, var(--wood-dark) 100%);
  }
  .line {
    position: absolute; left: 0; width: 1200px; text-align: center;
    white-space: nowrap; transform: translateY(-50%);
  }
  .brand-name {
    font-family: "Advent Pro", sans-serif; font-weight: 400;
    font-size: 112px; letter-spacing: 1px; top: 367px;
  }
  .headline {
    font-family: "Advent Pro", sans-serif; font-weight: 300;
    font-size: 132px; letter-spacing: 2px; top: 1426px;
  }
  .body-copy {
    font-family: "Yanone Kaffeesatz", sans-serif; font-weight: 300;
    font-size: 52px;
  }
  .highlight {
    font-family: "Dosis", sans-serif; font-weight: 800;
    font-size: 74px; color: var(--accent);
  }
  .contact {
    font-family: "Yanone Kaffeesatz", sans-serif; font-weight: 300;
    font-size: 40px;
  }
  .contact-name { font-weight: 700; font-size: 42px; }
</style>
</head>
<body>
  <div class="wood-surface" role="img" aria-label="Helle Holzmaserung als Hintergrund"></div>

  <div class="line brand-name">Restaurant Tovelo</div>

  <h1 class="line headline">STUZZICHINI</h1>

  <p class="line body-copy" style="top:1579px">Den typischen Apéro aus Italien gibt's</p>
  <p class="line highlight" style="top:1692px">Dienstags - Donnerstag</p>
  <p class="line highlight" style="top:1814px">ab 17.30 bis 19.00 Uhr</p>
  <p class="line body-copy" style="top:1960px">zu jedem Getränk Gratis Dazu.</p>
  <p class="line body-copy" style="top:2054px">Von Foccacia über Oliven bis zu</p>
  <p class="line body-copy" style="top:2147px">Lachsbrötchen- lassen Sie sich jede</p>
  <p class="line body-copy" style="top:2241px">Woche von neuen Leckerbissen</p>
  <p class="line body-copy" style="top:2333px">aus der Küche der Restaurant Tovelo</p>
  <p class="line highlight" style="top:2465px">überraschen!</p>

  <address style="font-style:normal">
    <div class="line contact contact-name" style="top:2794px">Restaurant-Tovelo</div>
    <div class="line contact" style="top:2849px">Lindenweg 12</div>
    <div class="line contact" style="top:2904px">8610 Talbach</div>
    <div class="line contact" style="top:2959px">Tel: 044 581 27 90</div>
    <div class="line contact" style="top:3016px">info@restaurant-tovelo.ch</div>
    <div class="line contact" style="top:3072px">www.restaurant-tovelo.ch</div>
  </address>
</body>
</html>
```